Business card for our large format printing and installation business

We want a professional looking business card for our business. We manufacture and install Signs.

On the back of the card add this info
Large Format Graphics Printing & Installations, Event Graphics, Banners, Posters, Vehicle Fleet Graphics, Boat Wraps, Wall Murals, Decals,Displays,Signs,Plaques,Digital Signs

On the Front of the card add the Tallowfern Signs logo, plus On the back of the card add the Orange Tallowfern Wraps logo. The 2 vector logos are attached to the design brief.

Target Market(s)

Local business owners

Contact Information for Business Card

Colors
f37122
f68d4e
f9ba93

Requirements
Must have
• On the Front of the card add the Tallowfern Signs logo, plus On the back of the card add the Orange Tallowfern Wraps logo. The 2 vector logos are attached to the design brief.

```html
<!DOCTYPE html>
<html lang="en">
<head>
<meta charset="utf-8">
<title>Tallowfern Wraps – Business Card</title>
<link rel="stylesheet" href="https://fonts.googleapis.com/css2?family=Chakra+Petch:wght@500;600;700&display=swap">
<style>
  :root {
    --page-bg: #3a3a3a;
    --yellow: #f9d52a;
    --orange: #f37122;
    --orange-mid: #f38a22;
    --ink: #1c1c1c;
    --card-white: #f0f0f0;
  }
  * { margin: 0; padding: 0; box-sizing: border-box; }
  html, body { width: 1200px; height: 900px; overflow: hidden; }
  body {
    background: var(--page-bg);
    font-family: "Chakra Petch", sans-serif;
    position: relative;
  }
  .card {
    position: absolute;
    left: 311px;
    width: 577px;
    height: 328px;
    box-shadow: 0 6px 14px rgba(0,0,0,0.45);
  }
  /* Back of card */
  .card-back {
    top: 98px;
    background: linear-gradient(180deg, var(--yellow) 0%, var(--orange-mid) 100%);
  }
  .card-back .wordmark {
    position: absolute;
    top: 128px;
    left: 0; right: 0;
    text-align: center;
    font-size: 46px;
    font-weight: 700;
    color: var(--ink);
    line-height: 1;
  }
  .services {
    position: absolute;
    top: 254px;
    left: 30px; right: 30px;
    text-align: center;
    font-size: 15.5px;
    font-weight: 600;
    color: var(--ink);
    line-height: 19.5px;
  }
  .services .sep { font-weight: 500; padding: 0 5px; }
  /* Front of card */
  .card-front {
    top: 472px;
    background: var(--card-white);
  }
  .card-front .wordmark {
    position: absolute;
    top: 52px;
    right: 35px;
    font-size: 30px;
    font-weight: 700;
    color: var(--orange);
    line-height: 1;
  }
  .person-name {
    position: absolute;
    top: 152px;
    left: 29px;
    font-size: 18px;
    font-weight: 700;
    color: var(--orange);
  }
  .divider {
    position: absolute;
    top: 188px;
    left: 29px;
    width: 514px;
    height: 2px;
    background: var(--orange);
  }
  .contact-list {
    position: absolute;
    top: 202px;
    left: 29px;
    list-style: none;
    font-size: 15px;
    font-weight: 500;
    color: var(--ink);
    line-height: 23px;
  }
  .contact-list li { display: flex; align-items: center; gap: 8px; }
  .contact-list svg { width: 14px; height: 14px; fill: var(--orange); flex: none; }
  .contact-list .label { color: var(--orange); }
  .address {
    position: absolute;
    top: 248px;
    right: 34px;
    text-align: right;
    font-size: 15px;
    font-weight: 500;
    color: var(--orange);
    line-height: 24px;
    font-style: normal;
  }
  .base-band {
    position: absolute;
    left: 0; right: 0; bottom: 0;
    height: 14px;
    background: linear-gradient(180deg, var(--yellow), var(--orange-mid));
  }
</style>
</head>
<body>
  <section class="card card-back" aria-label="Card back">
    <div class="wordmark">Tallowfern Wraps</div>
    <p class="services">
      Large Format Graphics Printing &amp; Installations<span class="sep">|</span>Event Graphics<br>
      Banners Posters<span class="sep">|</span>Vehicle Fleet Graphics<span class="sep">|</span>Boat Wraps<span class="sep">|</span>Wall<br>
      Murals&nbsp;&nbsp; Decals<span class="sep">|</span>Displays<span class="sep">|</span>Signs<span class="sep">|</span>Plaques<span class="sep">|</span>Digital Signs
    </p>
  </section>

  <section class="card card-front" aria-label="Card front">
    <div class="wordmark">Tallowfern Signs</div>
    <h1 class="person-name">Marco Delgado</h1>
    <div class="divider"></div>
    <ul class="contact-list">
      <li><svg viewBox="0 0 24 24"><path d="M6.6 10.8a15.5 15.5 0 0 0 6.6 6.6l2.2-2.2c.3-.3.7-.4 1-.2 1.1.4 2.3.6 3.6.6.6 0 1 .4 1 1V20c0 .6-.4 1-1 1A17 17 0 0 1 3 4c0-.6.4-1 1-1h3.5c.6 0 1 .4 1 1 0 1.3.2 2.5.6 3.6.1.3 0 .7-.2 1z"/></svg>954-555-0182 <span class="label">(Office)</span></li>
      <li><svg viewBox="0 0 24 24"><path d="M6.6 10.8a15.5 15.5 0 0 0 6.6 6.6l2.2-2.2c.3-.3.7-.4 1-.2 1.1.4 2.3.6 3.6.6.6 0 1 .4 1 1V20c0 .6-.4 1-1 1A17 17 0 0 1 3 4c0-.6.4-1 1-1h3.5c.6 0 1 .4 1 1 0 1.3.2 2.5.6 3.6.1.3 0 .7-.2 1z"/></svg>786-555-0147 <span class="label">(Direct)</span></li>
      <li><svg viewBox="0 0 24 24"><path d="M2 5h20v14H2z M2 5l10 8 10-8" /><path d="M2 5h20l-10 8z" fill="#f0f0f0"/></svg>marco@tallowfern.net</li>
      <li><svg viewBox="0 0 24 24"><path d="M12 2a10 10 0 1 0 0 20 10 10 0 0 0 0-20zm6.9 9h-3a15 15 0 0 0-1.3-5.5A8 8 0 0 1 18.9 11zM12 4.1c.9 1.3 1.7 3.6 1.9 6.9h-3.8c.2-3.3 1-5.6 1.9-6.9zM9.4 5.5A15 15 0 0 0 8.1 11h-3a8 8 0 0 1 4.3-5.5zM5.1 13h3a15 15 0 0 0 1.3 5.5A8 8 0 0 1 5.1 13zM12 19.9c-.9-1.3-1.7-3.6-1.9-6.9h3.8c-.2 3.3-1 5.6-1.9 6.9zm2.6-1.4a15 15 0 0 0 1.3-5.5h3a8 8 0 0 1-4.3 5.5z"/></svg>www.Tallowfernwraps.com</li>
    </ul>
    <address class="address">1480 Harbor Mill Road #4<br>Coral Bend, FL 33090</address>
    <div class="base-band"></div>
  </section>
</body>
</html>
```